Corporate Business Card

Very professional, Modern, Not to busy, include phone address email, website
(253) 555-0174, 61807 19th Street N, Kent, WA 98517, marcus@kestrelbayholding.com, brelvanindustries.com

Target Market(s)

Manufacturing

Industry/Entity Type

Aero, machining, manufacturing, Off road racing

Contact Information for Business Card

Phone, address email, website

```html
<!DOCTYPE html>
<html lang="en">
<head>
<meta charset="utf-8">
<title>Brelvan Industries – Business Card</title>
<link href="https://fonts.googleapis.com/css2?family=Questrial&display=swap" rel="stylesheet">
<style>
  :root {
    --navy: #17356b;
    --white: #ffffff;
    --page: #ffffff;
  }
  * { margin: 0; padding: 0; box-sizing: border-box; }
  html, body {
    width: 1200px;
    height: 686px;
    overflow: hidden;
    background: var(--page);
  }
  .canvas {
    position: relative;
    width: 1200px;
    height: 686px;
    font-family: "Questrial", "Century Gothic", sans-serif;
  }
  .card {
    position: absolute;
    left: 43px;
    top: 42px;
    width: 1113px;
    height: 602px;
    border: 2px solid var(--navy);
    border-radius: 40px;
    overflow: hidden;
    background: var(--white);
  }
  .brand {
    position: absolute;
    left: 0;
    right: 0;
    top: 138px;
    text-align: center;
    color: var(--navy);
    font-size: 50px;
    letter-spacing: 1px;
    line-height: 1;
  }
  .contact-band {
    position: absolute;
    left: 0;
    right: 0;
    top: 299px;
    bottom: 0;
    background: var(--navy);
  }
  .icon-row {
    position: absolute;
    left: 286px;
    top: 42px;
  }
  .contact-text {
    position: absolute;
    top: 144px;
    left: 0;
    right: 0;
    color: var(--white);
    font-size: 27px;
    line-height: 45px;
  }
  .contact-left {
    position: absolute;
    right: 572px;
    text-align: right;
    white-space: nowrap;
  }
  .contact-right {
    position: absolute;
    left: 569px;
    text-align: left;
    white-space: nowrap;
  }
</style>
</head>
<body>
<div class="canvas">
  <div class="card">
    <div class="brand">Brelvan Industries</div>

    <div class="contact-band">
      <svg class="icon-row" width="545" height="50" viewBox="0 0 545 50" aria-hidden="true">
        <line x1="0" y1="25" x2="545" y2="25" stroke="#ffffff" stroke-width="2"/>
        <!-- phone -->
        <circle cx="160" cy="25" r="23" fill="#ffffff"/>
        <path d="M152 14 c-3 1 -4 4 -3 8 c2 7 7 13 14 15 c3 1 6 0 7 -3 l-4 -4 c-1 -1 -2 -1 -3 0 l-2 2 c-3 -1 -6 -4 -7 -7 l2 -2 c1 -1 1 -2 0 -3 z" fill="none" stroke="var(--navy)" stroke-width="2" stroke-linejoin="round"/>
        <path d="M162 15 a8 8 0 0 1 7 7 M162 10 a13 13 0 0 1 12 12" fill="none" stroke="var(--navy)" stroke-width="2" stroke-linecap="round"/>
        <!-- envelope -->
        <circle cx="232" cy="25" r="23" fill="#ffffff"/>
        <rect x="220" y="16" width="24" height="17" rx="2" fill="none" stroke="var(--navy)" stroke-width="2"/>
        <path d="M220 17 l12 9 l12 -9 M220 33 l9 -8 M244 33 l-9 -8" fill="none" stroke="var(--navy)" stroke-width="2" stroke-linejoin="round"/>
        <!-- pin -->
        <circle cx="307" cy="25" r="23" fill="#ffffff"/>
        <path d="M307 35 c-6 -7 -9 -12 -9 -16 a9 9 0 0 1 18 0 c0 4 -3 9 -9 16 z" fill="var(--navy)"/>
        <circle cx="307" cy="19" r="3.5" fill="#ffffff"/>
        <ellipse cx="307" cy="37" rx="8" ry="2.5" fill="none" stroke="var(--navy)" stroke-width="1.8"/>
        <!-- globe -->
        <circle cx="381" cy="25" r="23" fill="#ffffff"/>
        <circle cx="381" cy="25" r="12" fill="none" stroke="var(--navy)" stroke-width="2"/>
        <ellipse cx="381" cy="25" rx="5" ry="12" fill="none" stroke="var(--navy)" stroke-width="1.8"/>
        <path d="M369 25 h24 M371 19 h20 M371 31 h20" stroke="var(--navy)" stroke-width="1.6"/>
      </svg>

      <div class="contact-text">
        <div class="contact-left">
          <div class="phone">(253) 555-0174, 61807</div>
          <div class="email">marcus@kestrelbayholding.com</div>
        </div>
        <div class="contact-right">
          <div class="website">brelvanindustries.com</div>
          <div class="address">19th Street N, Kent, WA 98517</div>
        </div>
      </div>
    </div>
  </div>
</div>
</body>
</html>
```